Business Card Design Project

Hello,

We have just created our new COMPANY LOGO via Pixel Harbor and would not like to turn our attention to new Business Cards.

We are a printing company based in Singapore & Las Vegas. We specialize in blue-print printing for the Architectural, Engineering and Construction industries

The design should be simple, professional, clean and organized.

The Business Cards should "pop" when seen and will hopefully be something that makes you look twice.

We have two different Pan-tones that we use for our company, feel free to use them if you think they will work for your design?

Orange: PMS 021
Gray: PMS 431

I have attached our current logo for your use and reference which should obvious be on our business cards.

Considering we have two locations on different continents, we need business cards templates where the address details need to be interchangeable for each different location (total 2)

First one:
38 Merrow Lane #03-11 to #03-15
Singapore 528473
Tel : +65 6847-3920
Fax : +65 6843-7702

Second one:
2381 W. Tanfield Rd, Suite 204
Las Vegas, Nevada 89152
Tel : (702) 555-4137
Fax : (702) 555-4189

We would also like to list a few of our key services on the card. Here are a few examples to get you going.

Plan Printing & Plotting
Digital Colour Printing
Cadline Printing
Specialty Book Making
Scanning & Archiving
Collection & Delivey

This is the first time i have requested for business cards to be created so please let me know if you require any additional information.
Many Thanks,
Tobin
Updates

Project Deadline Extended
Reason: It took us longer than expected to finalize our Company Logo We look forward to receiving your designs.

Target Market(s)

Our Target Market is construction related people.
Construction
Architecture
Engineering

Industry/Entity Type

Printing

Font styles to use
Other font styles liked:
• Times New Roman

Colors
faa54b
ffffff

Requirements
Must have
• The business card must have our Company Logo (attached)
The font used must be Times New Roman
Should not have
• Playful images of print designs and/or logos

```html
<!DOCTYPE html>
<html lang="en">
<head>
<meta charset="utf-8">
<title>Kestrel Plan Works – Business Card</title>
<link rel="stylesheet" href="https://fonts.googleapis.com/css2?family=Tinos:ital,wght@0,400;0,700;1,700&display=swap">
<style>
  :root {
    --brand-orange: #f9a54e;
    --ink: #000000;
    --paper: #ffffff;
    --card-edge: #3a3a3a;
  }
  * { margin: 0; padding: 0; box-sizing: border-box; }
  html, body {
    width: 1200px;
    height: 1001px;
    overflow: hidden;
    background: var(--paper);
    font-family: "Tinos", "Times New Roman", serif;
    color: var(--ink);
  }
  .canvas { position: relative; width: 1200px; height: 1001px; }

  .card {
    position: absolute;
    left: 29px; top: 197px;
    width: 1137px; height: 608px;
    border: 1px solid var(--card-edge);
    border-radius: 14px;
    background: var(--paper);
  }
  .brand-panel {
    position: absolute;
    left: 29px; top: 197px;
    width: 622px; height: 608px;
    background: var(--brand-orange);
    border-radius: 14px 12px 12px 14px;
  }

  .company-name {
    position: absolute;
    left: 0; width: 622px;
    top: 390px;
    text-align: center;
    font-weight: 700;
    font-size: 52px;
    line-height: 1;
  }
  .group-line {
    position: absolute;
    left: 0; width: 622px;
    top: 293px;
    text-align: center;
    font-style: italic;
    font-weight: 700;
    font-size: 28px;
    line-height: 1;
  }
  .divider {
    position: absolute;
    left: 23px; top: 442px;
    width: 576px; height: 3px;
    background: var(--paper);
  }
  .services {
    position: absolute;
    top: 474px; left: 0;
    width: 622px;
    list-style: none;
    font-size: 21px;
    line-height: 1;
  }
  .services li { position: absolute; white-space: nowrap; transform: translateX(-50%); }

  .contact {
    position: absolute;
    left: 700px; top: 343px;
    font-weight: 700;
    font-size: 44px;
    line-height: 64px;
    white-space: nowrap;
  }
</style>
</head>
<body>
<div class="canvas">
  <div class="card"></div>
  <section class="brand-panel">
    <p class="company-name" style="top:240px;">Kestrel Plan Works</p>
    <p class="group-line">A Member of the Kestrel Group of Companies</p>
    <div class="divider"></div>
    <ul class="services">
      <li style="left:213px; top:0;">Plan Printing &amp; Plotting</li>
      <li style="left:471px; top:0;">Digital Colour Printing</li>
      <li style="left:203px; top:39px;">Cadline Printing</li>
      <li style="left:444px; top:39px;">Specialty Book Making</li>
      <li style="left:213px; top:78px;">Scanning &amp; Archiving</li>
      <li style="left:471px; top:78px;">Collection &amp; Delivey</li>
    </ul>
  </section>
  <address class="contact" style="font-style:normal;">
    38 Merrow Lane<br>
    #03-11 to #03-15<br>
    Singapore 528473<br>
    Tel : +65 6847-3920<br>
    Fax : +65 6843-7702
  </address>
</div>
</body>
</html>
```